Unique Home Cooking School needs Wordpress Design

We need a wordpress design for our small business based in Singapore called Brisk Ladles. It is a unique cooking school where the cooking course menu is completely customised to our client's preference/lifestyle/requests. More information can be found on our site: briskladles.example

We are looking for something simple and easy to navigate. We are currently using a free template which we have customised ourselves. As the business is growing, we are looking to have a site more suited to our needs. The site should also be photo friendly, as we often post up photos of our food. It should also be social media integrated as a lot of our business is driven by PQ.

The look and feel should really reflect the personalities of both owners - like the logo. Please feel free to contact us if you need more clarification.

Target Market(s)

Our target audience are usually female, with children, aged 25 - 45.
They are either stay-at-home mums or full-time mums that are keen to do more for the family.

Industry/Entity Type

Small Business

Requirements
Must have
• The wordpress design has to be able to accommodate food photos on every page.
It also needs to be able to support social media feeds within the site.
Should not have
• Design should not have any chef-like design elements as we are not chefs. We are two stay-home-mums wanting to impart skills to other stay-home-mums or domestic helpers.

```html
<!DOCTYPE html>
<html lang="en">
<head>
<meta charset="utf-8">
<title>Brisk Ladles – Customised Hands On Cooking Classes</title>
<link rel="stylesheet" href="https://fonts.googleapis.com/css2?family=Oswald:wght@300;400&family=Source+Sans+3:wght@400;600&family=Comfortaa:wght@400&display=swap">
<style>
  :root {
    --page-bg: #ffffff;
    --hero-dark: #2b2622;
    --hero-brown: #5a4334;
    --hero-check: #3c4a6b;
    --hero-plate: #8d8f93;
    --overlay: rgba(40, 36, 34, 0.55);
    --text-light: #ffffff;
    --text-dark: #222222;
    --accent-pink: #e0457b;
    --share-navy: #3b5b99;
    --share-sky: #1da1e2;
    --share-coral: #dc4a38;
    --share-crimson: #cb2027;
    --card-border: #ececec;
    --dot-idle: rgba(255, 255, 255, 0.5);
  }
  * { box-sizing: border-box; margin: 0; padding: 0; }
  html, body {
    width: 1200px; height: 703px; overflow: hidden;
    background: var(--page-bg);
    font-family: "Source Sans 3", "Source Sans Pro", Arial, sans-serif;
  }
  .site { position: relative; width: 1200px; height: 703px; overflow: hidden; }

  .hero {
    position: absolute; left: 0; top: 0; width: 1200px; height: 505px;
  }
  .hero-photo {
    position: absolute; inset: 0;
    background:
      radial-gradient(circle at 930px 250px, #a9aaac 0, var(--hero-plate) 150px, transparent 240px),
      radial-gradient(circle at 60px 40px, #f2efe9 0, #e8e3dc 110px, transparent 150px),
      radial-gradient(circle at 430px 420px, #e9dcc4 0, #d8c4a0 70px, transparent 110px),
      linear-gradient(135deg, var(--hero-brown) 0%, var(--hero-dark) 30%, var(--hero-check) 55%, #2f3a55 75%, var(--hero-brown) 100%);
  }
  .hero-panel {
    position: absolute; left: 181px; top: 116px; width: 836px; height: 220px;
    background: var(--overlay);
    color: var(--text-light); text-align: center;
    padding-top: 32px;
  }
  .hero-title {
    font-family: "Oswald", "Arial Narrow", sans-serif;
    font-weight: 300; font-size: 35px; letter-spacing: 0.3px; line-height: 1.1;
    text-transform: uppercase;
  }
  .hero-text {
    width: 740px; margin: 14px auto 0;
    font-size: 14px; line-height: 1.45;
  }
  .hero-button {
    display: inline-block; margin-top: 16px;
    padding: 6px 18px; border: 1px solid var(--text-light);
    font-size: 14px; color: var(--text-light); text-decoration: none;
  }
  .slider-arrow {
    position: absolute; top: 243px; width: 16px; height: 24px;
  }
  .slider-arrow.prev { left: 22px; }
  .slider-arrow.next { right: 22px; }
  .slider-dots {
    position: absolute; top: 468px; left: 50%; transform: translateX(-50%);
    display: flex; gap: 7px;
  }
  .slider-dots span { width: 6px; height: 6px; border-radius: 50%; background: var(--dot-idle); }
  .slider-dots span.active { background: var(--text-light); }

  .share-bar {
    position: absolute; left: 0; top: 313px; width: 29px;
    display: flex; flex-direction: column;
  }
  .share-button { display: block; width: 29px; height: 29px; }
  .share-button.first { background: var(--share-navy); }
  .share-button.second { background: var(--share-sky); }
  .share-button.third { background: var(--share-coral); }
  .share-button.fourth { background: var(--share-crimson); }

  .featured {
    position: absolute; left: 0; top: 505px; width: 1200px; height: 198px;
  }
  .brand {
    position: absolute; left: 235px; top: 50px; width: 225px;
    display: flex; align-items: center; gap: 10px;
    font-family: "Comfortaa", "Source Sans 3", sans-serif;
    font-size: 26px; color: var(--text-dark); white-space: nowrap;
  }
  .brand-mark { width: 22px; height: 22px; border-radius: 50%; background: var(--accent-pink); flex: none; }
  .card {
    position: absolute; top: 14px; width: 240px; height: 184px;
    border: 1px solid var(--card-border); border-bottom: 0; background: var(--page-bg);
  }
  .card.cupcake { left: 477px; }
  .card.dish { left: 760px; }
  .card-photo { width: 100%; height: 148px; }
  .cupcake .card-photo { background: linear-gradient(160deg, #d4482e 0%, #7a3a1e 45%, #6ba33a 70%, #c43a24 100%); }
  .dish .card-photo { background: linear-gradient(150deg, #2d2f33 0%, #4a4f50 50%, #6a5a3e 100%); }
  .card-title {
    padding-top: 8px; text-align: center;
    font-family: "Oswald", "Arial Narrow", sans-serif;
    font-weight: 400; font-size: 15px; line-height: 20px;
    color: var(--accent-pink); text-transform: uppercase;
  }
</style>
</head>
<body>
<div class="site">
  <section class="hero">
    <div class="hero-photo" role="img" aria-label="Overhead photo of granola bowls with yoghurt, cherries, strawberries and peanuts on a blue gingham tablecloth with woven placemats"></div>
    <div class="hero-panel">
      <h1 class="hero-title">Customised Hands On Cooking Classes.</h1>
      <p class="hero-text">In our cooking lessons we will guide you step by step to help break down the barriers and increase your confidence in the kitchen. As our lessons are conducted in the comfort of your own home we can show you how to work with the equipment and appliances you have. Learn how to cook and prepare healthy meals today!</p>
      <a class="hero-button" href="#">Learn More</a>
    </div>
    <svg class="slider-arrow prev" viewBox="0 0 16 24" aria-label="Previous slide"><polyline points="12,3 4,12 12,21" fill="none" stroke="#fff" stroke-width="2"/></svg>
    <svg class="slider-arrow next" viewBox="0 0 16 24" aria-label="Next slide"><polyline points="4,3 12,12 4,21" fill="none" stroke="#fff" stroke-width="2"/></svg>
    <div class="slider-dots"><span class="active"></span><span></span><span></span></div>
    <nav class="share-bar" aria-label="Share">
      <a class="share-button first" href="#" aria-label="Share"></a>
      <a class="share-button second" href="#" aria-label="Share"></a>
      <a class="share-button third" href="#" aria-label="Share"></a>
      <a class="share-button fourth" href="#" aria-label="Share"></a>
    </nav>
  </section>

  <section class="featured">
    <div class="brand"><span class="brand-mark"></span>Brisk Ladles</div>
    <article class="card cupcake">
      <div class="card-photo" role="img" aria-label="Photo of chocolate cupcakes in green and red paper cases"></div>
      <h2 class="card-title">Cupcake</h2>
    </article>
    <article class="card dish">
      <div class="card-photo" role="img" aria-label="Photo of a plated dish on a dark table"></div>
    </article>
  </section>
</div>
</body>
</html>
```